Vemtra Group: Business Card for a high end technology company

We need a cool new design for our business cards using our cloud logo. We are a technology consulting business. We pride ourselves on be the best of the best. We mainly focus on cloud solutions and managed services. We need a business card that sets us apart from the other technology companies in the area and allows us to stand out.

Target Market(s)

Technology departments, CIO, CEOs, and Information Technology Staff.

Industry/Entity Type

Information Technology

Contact Information for Business Card

Must have the logo and our name.
Must have employee name, email address, office phone, cell phone and website.
Need to have all info on one side a cool design on backside.

Font styles to use
Serif
Sans Serif

Requirements
Must have
• Must have the logo and our name.
• Must have employee name, email address, office phone, cell phone and website.
• Need to have all info on one side a cool design on back side.
• Must be a crisp clean design, not too busy or confusing.

```html
<!DOCTYPE html>
<html lang="en">
<head>
<meta charset="utf-8">
<title>Vemtra Group – Business Card</title>
<link href="https://fonts.googleapis.com/css2?family=Quicksand:wght@500&family=Montserrat:wght@700&family=Arimo:wght@400&display=swap" rel="stylesheet">
<style>
  :root {
    --backdrop: #e9e6e1;
    --card-white: #ffffff;
    --charcoal: #3a393b;
    --ink: #1c1c1e;
    --blue-deep: #2f78c8;
    --blue-light: #5ccdf3;
    --paper-edge: #d9d9d9;
  }
  * { margin: 0; padding: 0; box-sizing: border-box; }
  html, body { width: 1200px; height: 892px; overflow: hidden; background: var(--backdrop); }
  .canvas { position: relative; width: 1200px; height: 892px; }

  .card {
    position: absolute;
    left: 290px;
    width: 620px;
    height: 354px;
    overflow: hidden;
    box-shadow: 0 2px 0 var(--paper-edge), 0 10px 24px rgba(0,0,0,.18);
  }
  .card--back { top: 70px; background: var(--charcoal); }
  .card--front { top: 468px; background: var(--card-white); }

  /* Back side */
  .back-brand {
    position: absolute; inset: 0;
    display: flex; flex-direction: column; align-items: center; justify-content: center;
    color: var(--card-white);
  }
  .brand-row { display: flex; align-items: center; gap: 16px; }
  .brand-dot { width: 22px; height: 22px; border-radius: 50%; background: var(--blue-light); }
  .brand-name {
    font-family: 'Quicksand', sans-serif; font-weight: 500;
    font-size: 58px; letter-spacing: 0.5px; line-height: 1;
  }
  .brand-url {
    font-family: 'Montserrat', sans-serif; font-weight: 700;
    font-size: 15px; letter-spacing: 1px; margin-top: 14px;
  }

  /* Front side */
  .front-stripes { position: absolute; inset: 0; }
  .front-brand { position: absolute; left: 40px; top: 46px; color: var(--ink); }
  .front-brand .brand-name { font-size: 48px; }
  .front-brand .brand-dot { width: 18px; height: 18px; background: var(--blue-deep); }
  .front-brand .brand-url { font-size: 13px; margin-top: 10px; margin-left: 34px; }

  .contact {
    position: absolute; right: 28px; top: 222px;
    text-align: right; color: var(--ink);
  }
  .contact-name {
    font-family: 'Montserrat', sans-serif; font-weight: 700;
    font-size: 26px; letter-spacing: 0.5px; line-height: 1; margin-bottom: 8px;
  }
  .contact-list { list-style: none; font-family: 'Arimo', sans-serif; font-size: 14px; }
  .contact-list li {
    display: flex; justify-content: flex-end; align-items: center; gap: 8px;
    height: 18px;
  }
  .icon { width: 13px; height: 13px; flex: none; }
</style>
</head>
<body>
<div class="canvas">

  <section class="card card--back" aria-label="Card back">
    <div class="back-brand">
      <div class="brand-row">
        <span class="brand-dot"></span>
        <span class="brand-name">Vemtra Group</span>
      </div>
      <div class="brand-url">www.vemtragroup.com</div>
    </div>
  </section>

  <section class="card card--front" aria-label="Card front">
    <svg class="front-stripes" width="620" height="354" viewBox="0 0 620 354">
      <defs>
        <linearGradient id="blueSweep" x1="0" y1="0" x2="1" y2="0">
          <stop offset="0" stop-color="#2f78c8"/>
          <stop offset="1" stop-color="#5ccdf3"/>
        </linearGradient>
      </defs>
      <polygon points="0,176 620,196 620,208 0,190" fill="#3a393b"/>
      <polygon points="0,190 620,208 620,354 0,354" fill="url(#blueSweep)"/>
    </svg>

    <div class="front-brand">
      <div class="brand-row">
        <span class="brand-dot"></span>
        <span class="brand-name">Vemtra Group</span>
      </div>
      <div class="brand-url">www.vemtragroup.com</div>
    </div>

    <div class="contact">
      <div class="contact-name">Corin Maddox</div>
      <ul class="contact-list">
        <li>555.210.4837
          <svg class="icon" viewBox="0 0 13 13"><rect width="13" height="13" rx="2" fill="#1c1c1e"/><path d="M3 4.5 Q6.5 2 10 4.5 L9 6 L7.5 5.3 L5.5 5.3 L4 6 Z M4 7 h5 v3 h-5z" fill="#fff"/></svg></li>
        <li>555.318.2046
          <svg class="icon" viewBox="0 0 13 13"><rect width="13" height="13" rx="2" fill="#1c1c1e"/><rect x="4.5" y="2.5" width="4" height="8" rx="0.8" fill="#fff"/><rect x="5.3" y="3.5" width="2.4" height="5" fill="#1c1c1e"/></svg></li>
        <li>hello@vemtragroup.com
          <svg class="icon" viewBox="0 0 13 13"><rect width="13" height="13" rx="2" fill="#1c1c1e"/><rect x="2.5" y="3.5" width="8" height="6" fill="#fff"/><path d="M2.5 3.5 L6.5 7 L10.5 3.5" fill="none" stroke="#1c1c1e" stroke-width="0.9"/></svg></li>
        <li>www.vemtragroup.com
          <svg class="icon" viewBox="0 0 13 13"><rect width="13" height="13" rx="2" fill="#1c1c1e"/><circle cx="6.5" cy="6.5" r="3.8" fill="none" stroke="#fff" stroke-width="1"/><path d="M2.7 6.5 h7.6 M6.5 2.7 v7.6" stroke="#fff" stroke-width="0.8"/></svg></li>
        <li>480 Larkfield Ave Suite 200, Brennan, GA 30399
          <svg class="icon" viewBox="0 0 13 13"><rect width="13" height="13" rx="2" fill="#1c1c1e"/><path d="M6.5 2.5 a3 3 0 0 1 3 3 c0 2-3 5-3 5 s-3-3-3-5 a3 3 0 0 1 3-3z" fill="#fff"/><circle cx="6.5" cy="5.5" r="1.1" fill="#1c1c1e"/></svg></li>
      </ul>
    </div>
  </section>

</div>
</body>
</html>
```